Stationery Design Project

KT7 Staffing requires letterhead and business card designs for a company based in London. Just like the name, we're a management resourcing company, providing resources to third party companies. You can see www.kt7staffing-example.com for ideas on existing colour schemes and design concepts that have been implimented and agreed to. Ultimately the design should broadcast professionalism, safety and the concept of growth.

Target Market(s)

Financial institutes; friendly societies (All UK based)

Industry/Entity Type

Safety

Requirements
Must have
• Files produced should be print ready; and the text in them editable (eg address, name etc)

```html
<!DOCTYPE html>
<html lang="en">
<head>
<meta charset="utf-8">
<title>KT7 Staffing — Stationery</title>
<link href="https://fonts.googleapis.com/css2?family=Roboto:wght@400;700&display=swap" rel="stylesheet">
<style>
  :root {
    --teal: #1a9fae;
    --teal-light: #74c0dc;
    --ink: #2b2b2b;
    --muted: #555;
    --paper: #ffffff;
    --backdrop: #e9e7e4;
    --font: "Roboto", Arial, sans-serif;
  }
  * { box-sizing: border-box; margin: 0; padding: 0; }
  html, body { width: 1200px; height: 900px; overflow: hidden; }
  body { background: var(--backdrop); font-family: var(--font); color: var(--ink); position: relative; }

  .letterhead {
    position: absolute; left: 32px; top: 46px; width: 572px; height: 808px;
    background: var(--paper); box-shadow: 0 2px 8px rgba(0,0,0,.15);
  }
  .brand { display: flex; align-items: center; gap: 8px; }
  .brand-mark { width: 12px; height: 12px; background: var(--teal); }
  .brand-name { color: var(--teal); font-weight: 700; text-transform: uppercase; letter-spacing: .02em; }
  .letterhead .brand { position: absolute; left: 38px; top: 34px; }
  .letterhead .brand-name { font-size: 26px; }

  .contact-list { list-style: none; font-size: 9.5px; line-height: 12.5px; color: var(--ink); }
  .contact-list li { display: flex; align-items: center; gap: 8px; }
  .contact-list svg { width: 9px; height: 9px; fill: var(--teal); flex: none; }
  .letterhead .contact-list {
    position: absolute; left: 410px; top: 26px; padding-left: 0;
  }
  .letterhead .contact-list::after {
    content: ""; position: absolute; left: 14px; top: 0; width: 1px; height: 64px; background: var(--teal-light);
  }
  .letterhead .contact-list li { gap: 14px; }

  .letterhead-web {
    position: absolute; right: 130px; bottom: 19px; font-size: 9px; letter-spacing: .28em; color: var(--teal);
  }
  .letterhead-band {
    position: absolute; left: 0; right: 0; bottom: 0; height: 9px; background: var(--teal-light);
  }

  .card {
    position: absolute; top: 252px; width: 243px; height: 138px; border-radius: 9px; overflow: hidden;
    box-shadow: 0 2px 6px rgba(0,0,0,.15);
  }
  .card-front { left: 674px; background: var(--paper); }
  .card-front .brand { position: absolute; left: 14px; top: 16px; gap: 5px; }
  .card-front .brand-mark { width: 7px; height: 7px; }
  .card-front .brand-name { font-size: 12px; }
  .card-holder { position: absolute; left: 19px; top: 57px; }
  .card-holder-name { font-size: 9px; font-weight: 700; }
  .card-holder-role { font-size: 6.5px; color: var(--muted); margin-top: 1px; }
  .card-front .contact-list { position: absolute; left: 19px; top: 84px; font-size: 6px; line-height: 8.2px; }
  .card-front .contact-list li { gap: 6px; }
  .card-front .contact-list svg { width: 6px; height: 6px; }

  .card-back { left: 930px; background: linear-gradient(100deg, var(--teal) 0%, var(--teal-light) 100%); }
  .card-back .brand { position: absolute; left: 119px; top: 54px; gap: 6px; }
  .card-back .brand-mark { width: 8px; height: 8px; background: #fff; }
  .card-back .brand-name { color: #fff; font-size: 14px; }
  .card-back-web {
    position: absolute; right: 20px; bottom: 11px; font-size: 6.5px; letter-spacing: .25em; color: #fff;
  }
</style>
</head>
<body>
<svg width="0" height="0" style="position:absolute" aria-hidden="true">
  <symbol id="icon-mobile" viewBox="0 0 10 10"><rect x="2.5" y="0" width="5" height="10" rx="1"/></symbol>
  <symbol id="icon-phone" viewBox="0 0 10 10"><path d="M0 4 Q5 0 10 4 L9 5 L7 4 L3 4 L1 5 Z M2 6 H8 V10 H2 Z"/></symbol>
  <symbol id="icon-fax" viewBox="0 0 10 10"><rect x="0" y="3" width="10" height="7" rx="1"/><rect x="2" y="0" width="6" height="3"/></symbol>
  <symbol id="icon-mail" viewBox="0 0 10 10"><path d="M0 2 H10 V9 H0 Z M1 3 L5 6 L9 3 V3.6 L5 6.8 L1 3.6 Z" fill-rule="evenodd"/></symbol>
  <symbol id="icon-web" viewBox="0 0 10 10"><path d="M5 0 A5 5 0 1 0 5 10 A5 5 0 1 0 5 0 Z M5 1.2 A3.8 3.8 0 1 1 5 8.8 A3.8 3.8 0 1 1 5 1.2 Z M4.5 1 H5.5 V9 H4.5 Z M1 4.5 H9 V5.5 H1 Z" fill-rule="evenodd"/></symbol>
</svg>

<main class="letterhead">
  <div class="brand"><span class="brand-mark"></span><span class="brand-name">KT7 Staffing</span></div>
  <ul class="contact-list">
    <li><svg><use href="#icon-mobile"/></svg>020-555-0142</li>
    <li><svg><use href="#icon-phone"/></svg>020-555-0187</li>
    <li><svg><use href="#icon-fax"/></svg>020-555-0187</li>
    <li><svg><use href="#icon-mail"/></svg>ravi@kt7staffing-example.com</li>
    <li><svg><use href="#icon-web"/></svg>kt7staffing-example.com</li>
  </ul>
  <p class="letterhead-web">www.kt7staffing-example.com</p>
  <div class="letterhead-band"></div>
</main>

<section class="card card-front">
  <div class="brand"><span class="brand-mark"></span><span class="brand-name">KT7 Staffing</span></div>
  <div class="card-holder">
    <p class="card-holder-name">Ravi Holloway</p>
    <p class="card-holder-role">Director</p>
  </div>
  <ul class="contact-list">
    <li><svg><use href="#icon-mobile"/></svg>020-555-0142</li>
    <li><svg><use href="#icon-phone"/></svg>020-555-0187</li>
    <li><svg><use href="#icon-fax"/></svg>020-555-0187</li>
    <li><svg><use href="#icon-mail"/></svg>ravi@kt7staffing-example.com</li>
    <li><svg><use href="#icon-web"/></svg>kt7staffing-example.com</li>
  </ul>
</section>

<section class="card card-back">
  <div class="brand"><span class="brand-mark"></span><span class="brand-name">KT7 Staffing</span></div>
  <p class="card-back-web">www.kt7staffing-example.com</p>
</section>
</body>
</html>
```